Business Card Design Project

I require a business card with the following information on them for various different people;
name
m:
f:
e:
I have a logo already and will attached that. We are in the construction industry. I require something clean and simple but eye catching at the same time. You can use another colour with our logo if you like and you can style the logo as well if you wish. I am open.
Also it needs to be front and back design.
Industry/Entity Type
Construction
Requirements
Must have
- Logo, name, mobile, fax and email address.
Front and back design

```html
<!DOCTYPE html>
<html lang="en">
<head>
<meta charset="utf-8">
<title>Northfield Build Group – Business Cards</title>
<link rel="stylesheet" href="https://fonts.googleapis.com/css2?family=Questrial&family=Arimo:wght@400&display=swap">
<style>
  :root {
    --backdrop: #1b1b1d;
    --navy-light: #1f3a72;
    --navy: #142a5a;
    --navy-deep: #0a1838;
    --green: #7cc242;
    --grey-line: #c4c7cc;
    --white: #ffffff;
    --soft-white: #e9ebef;
  }
  * { box-sizing: border-box; margin: 0; padding: 0; }
  html, body {
    width: 1200px;
    height: 900px;
    overflow: hidden;
    background: var(--backdrop);
  }
  .canvas {
    position: relative;
    width: 1200px;
    height: 900px;
    background: var(--backdrop);
  }
  .card {
    position: absolute;
    width: 700px;
    height: 400px;
    background: radial-gradient(ellipse at 35% 20%, var(--navy-light) 0%, var(--navy) 45%, var(--navy-deep) 100%);
    box-shadow: 0 10px 30px rgba(0,0,0,0.55);
    overflow: hidden;
  }
  .card--info { left: 110px; top: 45px; }
  .card--front { left: 390px; top: 455px; }

  .wordmark {
    position: absolute;
    display: flex;
    align-items: center;
    gap: 14px;
    font-family: "Questrial", sans-serif;
    font-weight: 400;
    color: var(--green);
    white-space: nowrap;
  }
  .wordmark__square {
    display: block;
    background: var(--green);
  }
  .card--info .wordmark {
    left: 50%;
    top: 62px;
    transform: translateX(-50%);
    font-size: 34px;
  }
  .card--info .wordmark__square { width: 34px; height: 34px; }
  .card--front .wordmark {
    left: 50%;
    top: 50%;
    transform: translate(-50%, -50%);
    font-size: 40px;
  }
  .card--front .wordmark__square { width: 40px; height: 40px; }

  .holder {
    position: absolute;
    left: 40px;
    top: 178px;
    display: flex;
    align-items: baseline;
    gap: 10px;
    font-family: "Arimo", sans-serif;
  }
  .holder__name {
    font-family: "Questrial", sans-serif;
    font-size: 27px;
    color: var(--green);
    letter-spacing: 0.5px;
  }
  .holder__divider { font-size: 24px; color: var(--soft-white); }
  .holder__title { font-size: 19px; color: var(--white); }

  .rule {
    position: absolute;
    left: 0;
    width: 100%;
  }
  .rule--grey { top: 222px; height: 4px; background: var(--grey-line); }
  .rule--green { top: 230px; height: 3px; background: var(--green); }

  .contact {
    position: absolute;
    left: 0;
    width: 100%;
    top: 252px;
    font-family: "Arimo", sans-serif;
    font-size: 17px;
    line-height: 25px;
    color: var(--white);
    text-align: center;
  }
  .contact__label { color: var(--green); }
</style>
</head>
<body>
<main class="canvas">

  <section class="card card--info" aria-label="Card back with contact details">
    <div class="wordmark">
      <span class="wordmark__square"></span>
      <span class="wordmark__name">Northfield Build Group</span>
    </div>

    <div class="holder">
      <span class="holder__name">YOUR NAME</span>
      <span class="holder__divider">|</span>
      <span class="holder__title">Job Title</span>
    </div>

    <div class="rule rule--grey"></div>
    <div class="rule rule--green"></div>

    <div class="contact">
      <p><span class="contact__label">Address</span> : Street Name, City, State, Zip Code</p>
      <p><span class="contact__label">Mobile</span> : xxxxxxxxxx&nbsp;&nbsp;<span class="contact__label">Fax</span> : xxx xxx xxxx</p>
      <p><span class="contact__label">E-mail</span> : name@Website.com</p>
    </div>
  </section>

  <section class="card card--front" aria-label="Card front with company name">
    <div class="wordmark">
      <span class="wordmark__square"></span>
      <span class="wordmark__name">Northfield Build Group</span>
    </div>
  </section>

</main>
</body>
</html>
```